CBD online business for pets and pet parents needs a new website

We need a website for my new online business. I have left a job of 25 years to do my passion. Helping Pets Live healthy and happy lives. I would like to provide my story so that our customer will know why I have started this business-To help!We will be providing all natural CBD (Hemp) products, specialty items, memorials as well as some products for pet parents. We would like our landing page to have our mission, be informative and easy to navigate and maybe feature our treats and oils for pets. We will need a page for pet products, a page for pet memorials, a page for pet lover products and a page for pet parent products.

Target Market(s)

millennials, boomers, pet lovers

Coding

Coded - Design and coding required

Number of Pages Required

5+ page

Colors
33b8a4

Requirements
Nice to have
• diagram of hemp oil extract benefits for dogs and people

```html
<!DOCTYPE html>
<html lang="en">
<head>
<meta charset="utf-8">
<title>Kindred Paw – Helping Pets Live Healthy and Happy Lives</title>
<link href="https://fonts.googleapis.com/css2?family=Lato:ital,wght@0,300;0,400;0,700;1,400;1,700&display=swap" rel="stylesheet">
<style>
:root{
  --lime:#8cc63f;
  --lime-dark:#6fae22;
  --blue:#1a8ad4;
  --forest:#1f5a3a;
  --ink:#222;
  --text:#555;
  --muted:#8a8a8a;
  --line:#e3e3e3;
  --soft:#f3f4f3;
  --white:#fff;
}
*{margin:0;padding:0;box-sizing:border-box}
html,body{width:1200px;height:4406px;overflow:hidden}
body{font-family:'Lato',sans-serif;color:var(--ink);background:var(--white);position:relative}
.abs{position:absolute}
section,header,footer,nav{position:absolute;left:0;width:1200px}
.btn{position:absolute;display:flex;align-items:center;justify-content:center;background:var(--forest);color:var(--white);border-radius:26px;font-size:16px;letter-spacing:.3px}
.section-title{position:absolute;left:0;width:1200px;text-align:center;font-size:43px;font-weight:400;color:var(--ink)}
.underline{position:absolute;height:3px;background:var(--blue);width:104px;left:548px}
.photo{position:absolute}

/* top bar */
.topbar{top:0;height:94px;border-bottom:1px solid var(--line)}
.social-mini{top:20px;left:76px;display:flex;gap:17px}
.social-mini span{width:10px;height:10px;border-radius:50%;background:#9a9a9a;display:block}
.contact-line{font-size:15px;color:var(--text);display:flex;align-items:center;gap:12px;white-space:nowrap}
.account{top:20px;left:906px;font-size:14px;color:#8a8a8a;display:flex;gap:20px}
.cart{top:14px;left:1082px}
.badge{position:absolute;top:-4px;left:14px;width:18px;height:18px;border-radius:50%;background:var(--blue);color:#fff;font-size:11px;display:flex;align-items:center;justify-content:center}

/* nav */
.nav{top:99px;height:63px;background:var(--lime);border-bottom:3px solid #7fb232}
.nav a{position:absolute;top:22px;color:var(--white);font-size:15px;text-decoration:none;letter-spacing:.3px}
.nav a.active{font-weight:700}
.brand-circle{position:absolute;top:66px;left:535px;width:130px;height:130px;border-radius:50%;background:var(--white);box-shadow:0 2px 8px rgba(0,0,0,.15);display:flex;align-items:center;justify-content:center;text-align:center;font-size:17px;font-weight:700;color:var(--forest);line-height:1.2;z-index:2}

/* hero */
.hero{top:162px;height:576px;background:linear-gradient(90deg,#7a7560 0%,#a9a18a 30%,#e8e6e0 55%,#f5f4f1 100%)}
.hero-copy{left:632px;top:112px}
.hero h1{font-weight:400;font-size:58px;line-height:68px;color:var(--ink)}
.hero h1 .hl{color:var(--blue)}
.hero p{font-style:italic;font-size:17px;line-height:29px;color:#333;margin-top:16px;width:500px}

/* story */
.story{top:738px;height:522px}
.story h2{position:absolute;left:79px;top:56px;font-size:43px;font-weight:400}
.story .underline{left:79px;top:110px}
.story .lead{position:absolute;left:79px;top:140px;width:490px;font-style:italic;font-weight:700;font-size:16px;line-height:29px;color:#333}
.story .body{position:absolute;left:79px;top:216px;width:500px;font-size:13px;line-height:26px;color:var(--muted)}
.sq{position:absolute;width:24px;height:24px}
.round-photo{position:absolute;border-radius:50%}
.dot{position:absolute;border-radius:50%}

/* benefits */
.benefits{top:1260px;height:603px;background:linear-gradient(160deg,#c9c4bd 0%,#9a958c 45%,#b7b3ad 75%,#8e8a84 100%)}
.benefits .section-title{top:58px}
.benefits .underline{top:110px}
.hub{position:absolute;left:453px;top:210px;width:290px;height:290px;border-radius:50%;background:var(--white);border:2px dashed #cfd6cf;display:flex;align-items:center;justify-content:center;text-align:center;font-weight:700;font-size:24px;line-height:1.3;color:var(--forest)}
.benefit{position:absolute;height:71px;background:var(--white);box-shadow:0 2px 6px rgba(0,0,0,.08);display:flex;align-items:center;gap:12px;padding:0 16px;font-size:15px;line-height:24px;color:#444}
.benefit .num{flex:none;width:24px;height:20px;background:#e7f2d4;color:var(--forest);font-size:11px;font-weight:700;display:flex;align-items:center;justify-content:center}
.node{position:absolute;width:20px;height:20px;border-radius:50%;border:2px solid var(--blue);background:var(--white)}
.node::after{content:"";position:absolute;left:4px;top:4px;width:8px;height:8px;border-radius:50%;background:var(--blue)}

/* products */
.products{top:1863px;height:675px}
.products .section-title{top:58px}
.products .underline{top:112px}
.product{position:absolute;top:167px;width:239px;height:342px;border:1px solid #ececec;border-radius:4px;background:var(--white)}
.product.featured{box-shadow:0 3px 12px rgba(0,0,0,.12)}
.product .img{position:absolute;left:50px;top:21px;width:139px;height:171px;border-radius:4px;background:linear-gradient(180deg,#d8efed 0%,#bfe3df 50%,#c8c1b4 100%)}
.product .name{position:absolute;top:218px;width:100%;text-align:center;font-size:18px;color:#444}
.stars{color:#f2b21b;letter-spacing:1px}
.product .stars{position:absolute;top:245px;width:100%;text-align:center;font-size:16px}
.product .price{position:absolute;top:277px;width:100%;text-align:center;font-size:20px;color:#222;font-weight:700}
.product .price s{font-size:16px;color:#999;font-weight:400;margin-right:16px}
.add-cart{position:absolute;left:42px;top:95px;width:156px;height:38px;border-radius:20px;background:var(--forest);color:#fff;font-size:13px;font-weight:700;display:flex;align-items:center;justify-content:center;gap:8px}

/* testimonial */
.testimonial{top:2538px;height:603px;background:var(--soft)}
.testimonial .section-title{top:58px}
.testimonial .underline{top:112px}
.quote-mark{position:absolute;top:140px;left:0;width:1200px;text-align:center;font-size:110px;line-height:1;font-weight:700;color:var(--lime);font-family:Georgia,serif}
.testimonial .copy{position:absolute;left:252px;top:234px;width:696px;text-align:center;font-size:13.5px;line-height:26px;color:var(--muted)}
.testimonial .stars{position:absolute;top:330px;width:1200px;text-align:center;font-size:17px}
.avatar{position:absolute;border-radius:50%;background:linear-gradient(180deg,#d6dde0,#9fb0b8);border:3px solid var(--forest)}
.arrow{position:absolute;top:252px}
.client{position:absolute;top:518px;width:1200px;text-align:center;font-size:17px;color:#222}

/* blog */
.blog{top:3141px;height:593px}
.blog .section-title{top:58px}
.blog .underline{top:113px}
.post{position:absolute;top:169px;width:333px}
.post .img{position:relative;height:185px}
.date{position:absolute;left:10px;bottom:0;width:51px;height:58px;background:var(--forest);color:#fff;text-align:center;font-size:22px;font-weight:700;line-height:1;padding-top:10px}
.date small{display:block;font-size:11px;font-weight:400;margin-top:4px}
.post h3{margin:30px 0 0 2px;font-size:20px;font-weight:700;color:var(--lime-dark);letter-spacing:.2px}
.post p{margin:12px 0 0 2px;font-size:13.5px;line-height:26px;color:var(--muted);width:320px}
.post a{display:inline-block;margin:14px 0 0 2px;font-size:14px;color:var(--forest);text-decoration:underline}

/* newsletter */
.newsletter{top:3734px;height:274px;background:linear-gradient(90deg,#7cb729 0%,#8ec63f 55%,#a7d056 100%)}
.newsletter h2{position:absolute;top:60px;width:1200px;text-align:center;font-size:27px;font-weight:400;color:#fff}
.newsletter .sub{position:absolute;top:104px;width:1200px;text-align:center;font-size:13px;color:#fff}
.email-field{position:absolute;left:313px;top:147px;width:572px;height:62px;background:#fff;border-radius:4px;display:flex;align-items:center;justify-content:space-between;padding:0 24px;font-size:14px;color:#555}

/* footer */
.site-footer{top:4008px;height:398px}
.foot-brand{position:absolute;left:78px;top:88px;display:flex;align-items:center;gap:10px;font-size:18px;font-weight:700;color:var(--forest)}
.foot-brand i{width:16px;height:16px;border-radius:50%;background:var(--lime);display:block}
.foot-about{position:absolute;left:79px;top:150px;font-size:13px;line-height:26px;color:var(--muted);width:180px}
.col{position:absolute;top:62px}
.col h4{font-size:17px;font-weight:400;color:#222;margin-bottom:22px}
.col ul{list-style:none}
.col li{font-size:13px;color:var(--muted);line-height:25px}
.col li::before{content:"- ";color:#bbb}
.where div{display:flex;gap:20px;align-items:flex-start;font-size:13px;color:var(--muted);line-height:25px;margin-bottom:16px}
.socials{display:flex;gap:9px}
.socials span{width:40px;height:40px;border-radius:50%;display:block}
.copyright{position:absolute;top:316px;left:0;width:1200px;border-top:1px solid var(--line);padding-top:32px;text-align:center;font-size:13px;color:#b0b0b0}
</style>
</head>
<body>

<header class="topbar">
  <div class="abs social-mini"><span></span><span></span><span></span><span></span></div>
  <div class="abs contact-line" style="left:76px;top:50px">
    <svg width="18" height="18" viewBox="0 0 24 24"><path fill="#1a8ad4" d="M6.6 10.8a15.1 15.1 0 006.6 6.6l2.2-2.2c.3-.3.7-.4 1-.2 1.1.4 2.3.6 3.6.6.6 0 1 .4 1 1V20c0 .6-.4 1-1 1A17 17 0 013 4c0-.6.4-1 1-1h3.5c.6 0 1 .4 1 1 0 1.3.2 2.5.6 3.6.1.3 0 .7-.2 1z"/></svg>
    (123) 456 7890
  </div>
  <div class="abs account"><span>LOGIN</span><span>|</span><span>REGISTER</span></div>
  <div class="abs cart">
    <svg width="22" height="22" viewBox="0 0 24 24" fill="none" stroke="#222" stroke-width="2"><path d="M4 8h16l-1 13H5z"/><path d="M8 8V6a4 4 0 018 0v2"/></svg>
    <span class="badge">0</span>
  </div>
  <div class="abs contact-line" style="left:882px;top:50px">
    <svg width="20" height="16" viewBox="0 0 24 18"><rect x="1" y="1" width="22" height="16" rx="2" fill="#1a8ad4"/><path d="M1 2l11 8 11-8" stroke="#fff" stroke-width="2" fill="none"/></svg>
    hello@kindredpaw.example
  </div>
</header>

<nav class="nav">
  <a class="active" style="left:110px">HOME</a>
  <a style="left:224px">OUR STORY</a>
  <a style="left:381px">PRODUCTS</a>
  <a style="left:735px">BENEFITS</a>
  <a style="left:870px">BLOG</a>
  <a style="left:981px">CONTACT</a>
</nav>
<div class="brand-circle">KINDRED<br>PAW</div>

<section class="hero">
  <div class="photo" role="img" aria-label="Amber CBD oil bottle beside hemp buds on a wooden table" style="left:0;top:0;width:600px;height:576px;background:radial-gradient(ellipse at 60% 45%,#8a5a2a 0%,#6e5d3e 25%,rgba(0,0,0,0) 60%)"></div>
  <div class="abs hero-copy">
    <h1>HELPING PETS<br><span class="hl">LIVE HEALTHY</span> AND<br><span class="hl">HAPPY LIVES</span></h1>
    <p>Lorem ipsum dolor sit amet, consectetur adipiscing elit, sed eiusmod tempor incididunt ut labore et dolore magna aliqua.</p>
  </div>
  <div class="btn" style="left:630px;top:402px;width:155px;height:48px">LEARN MORE</div>
</section>

<section class="story">
  <h2>OUR STORY</h2>
  <div class="underline"></div>
  <p class="lead">Lorem ipsum dolor sit amet, consectetur adipiscing elit, sed eiusmod tempor incididunt ut labore et dolore magna aliqua.</p>
  <p class="body">Lorem ipsum dolor sit amet, consectetur adipiscing elit, sed deiusmod tempor incididunt ut labore et dolore magna aliqua. Ut enim ad minim veniam, quis nostrud exercitation ullamco laboris nisi ut aliquip ex ea commodo consequat. Duis aute irure dolor in reprehenderit in voluptate velit esse cillum dolore eu fugiat nulla pariatur. Excepteur sint occaecat cupidatat non proident, sunt in culpa qui officia deserunt mollit anim id est laborum.</p>
  <div class="btn" style="left:77px;top:405px;width:155px;height:52px">LEARN MORE</div>
  <div class="sq" style="left:20px;top:460px;background:var(--blue)"></div>
  <div class="sq" style="left:52px;top:460px;background:var(--forest)"></div>
  <div class="sq" style="left:52px;top:492px;background:var(--lime)"></div>

  <div class="round-photo" role="img" aria-label="Smiling woman hugging her dog" style="left:749px;top:54px;width:228px;height:228px;background:linear-gradient(160deg,#d9cbb8,#b08a5e)"></div>
  <div class="round-photo" role="img" aria-label="Cat sniffing a hemp leaf" style="left:638px;top:225px;width:228px;height:228px;border:4px solid #fff;background:linear-gradient(160deg,#cfe0c0,#8aa86e)"></div>
  <div class="round-photo" role="img" aria-label="Small dog wearing a bandana lying on a path" style="left:857px;top:225px;width:228px;height:228px;border:4px solid #fff;background:linear-gradient(160deg,#b9c3b0,#8b8a7c)"></div>
  <div class="dot" style="left:722px;top:177px;width:14px;height:14px;background:var(--blue)"></div>
  <div class="dot" style="left:726px;top:208px;width:8px;height:8px;background:var(--lime)"></div>
  <div class="dot" style="left:705px;top:206px;width:6px;height:6px;background:var(--forest)"></div>
  <div class="dot" style="left:986px;top:190px;width:18px;height:18px;background:var(--lime)"></div>
  <div class="dot" style="left:1107px;top:299px;width:8px;height:8px;background:var(--blue)"></div>
  <div class="dot" style="left:1100px;top:324px;width:6px;height:6px;background:var(--lime)"></div>
  <div class="dot" style="left:1108px;top:349px;width:14px;height:14px;background:var(--forest)"></div>
</section>

<section class="benefits" role="img" aria-label="Soft photo of a person holding a dog's paw behind the benefits diagram">
  <h2 class="section-title">CBD BENEFITS</h2>
  <div class="underline"></div>
  <svg class="abs" style="left:0;top:0" width="1200" height="603">
    <g stroke="#ffffff" stroke-width="1.5" fill="none" opacity=".8">
      <line x1="444" y1="223" x2="485" y2="285"/><line x1="403" y1="358" x2="463" y2="357"/><line x1="444" y1="490" x2="485" y2="430"/>
      <line x1="757" y1="223" x2="731" y2="285"/><line x1="795" y1="358" x2="753" y2="357"/><line x1="757" y1="490" x2="731" y2="430"/>
    </g>
  </svg>
  <div class="hub">KINDRED<br>PAW</div>
  <div class="node" style="left:465px;top:275px"></div>
  <div class="node" style="left:443px;top:347px"></div>
  <div class="node" style="left:465px;top:420px"></div>
  <div class="node" style="left:711px;top:275px"></div>
  <div class="node" style="left:733px;top:347px"></div>
  <div class="node" style="left:711px;top:420px"></div>
  <div class="benefit" style="left:150px;top:188px;width:294px"><span class="num">01</span>99.5% Pure CBD Extract</div>
  <div class="benefit" style="left:113px;top:323px;width:290px"><span class="num">02</span>Improve Life Quality</div>
  <div class="benefit" style="left:150px;top:458px;width:294px"><span class="num">03</span>Body's Natural<br>Endocannabinoid System</div>
  <div class="benefit" style="left:757px;top:188px;width:294px"><span class="num">04</span>99.5% Pure CBD Extract</div>
  <div class="benefit" style="left:795px;top:323px;width:290px"><span class="num">05</span>Time-Release Formula</div>
  <div class="benefit" style="left:757px;top:458px;width:294px"><span class="num">06</span>CBD Oil from Hemp is Legal<br>and Won't Get You High</div>
</section>

<section class="products">
  <h2 class="section-title">OUR PRODUCTS</h2>
  <div class="underline"></div>
  <div class="product featured" style="left:77px">
    <div class="img" role="img" aria-label="Pet CBD oil bottle with dropper" style="opacity:.45"></div>
    <div class="add-cart"><svg width="14" height="14" viewBox="0 0 24 24" fill="none" stroke="#fff" stroke-width="2"><path d="M4 8h16l-1 13H5z"/><path d="M8 8V6a4 4 0 018 0v2"/></svg>ADD TO CART</div>
    <div class="name">Lorem Ipsum</div><div class="stars">★★★★☆</div><div class="price"><s>$ 40</s>$ 35</div>
  </div>
  <div class="product" style="left:345px">
    <div class="img" role="img" aria-label="Pet CBD oil bottle with dropper"></div>
    <div class="name">Lorem Ipsum</div><div class="stars">★★★★☆</div><div class="price"><s>$ 40</s>$ 35</div>
  </div>
  <div class="product" style="left:614px">
    <div class="img" role="img" aria-label="Pet CBD oil bottle with dropper"></div>
    <div class="name">Lorem Ipsum</div><div class="stars">★★★★☆</div><div class="price"><s>$ 40</s>$ 35</div>
  </div>
  <div class="product" style="left:882px">
    <div class="img" role="img" aria-label="Pet CBD oil bottle with dropper"></div>
    <div class="name">Lorem Ipsum</div><div class="stars">★★★★☆</div><div class="price"><s>$ 40</s>$ 35</div>
  </div>
  <div class="btn" style="left:523px;top:564px;width:154px;height:48px">VIEW MORE</div>
</section>

<section class="testimonial">
  <h2 class="section-title">CLIENTS TESTIMONIAL</h2>
  <div class="underline"></div>
  <div class="quote-mark">“</div>
  <p class="copy">Lorem ipsum dolor sit amet, consectetur adipiscing elit, sed deiusmod tempor incididunt ut labore et dolore magna aliqua. Ut enim ad minim veniam, quis nostrud exercitation ullamco laboris nisi ut aliquip ex ea commodo consequat. Duis aute irure dolor in reprehenderit in voluptate velit esse</p>
  <div class="stars">★★★★☆</div>
  <svg class="arrow" style="left:176px" width="24" height="64" viewBox="0 0 24 64"><path d="M20 2L4 32l16 30" stroke="#333" stroke-width="2" fill="none"/></svg>
  <svg class="arrow" style="left:996px" width="24" height="64" viewBox="0 0 24 64"><path d="M4 2l16 30L4 62" stroke="#333" stroke-width="2" fill="none"/></svg>
  <div class="avatar" role="img" aria-label="Client portrait" style="left:446px;top:398px;width:76px;height:76px"></div>
  <div class="avatar" role="img" aria-label="Client portrait" style="left:546px;top:384px;width:104px;height:104px;border:4px solid #fff;box-shadow:0 0 0 3px var(--forest)"></div>
  <div class="avatar" role="img" aria-label="Client portrait" style="left:676px;top:398px;width:76px;height:76px"></div>
  <div class="client">- SAM RIVERA</div>
</section>

<section class="blog">
  <h2 class="section-title">RECENT BLOG</h2>
  <div class="underline"></div>
  <article class="post" style="left:77px">
    <div class="img" role="img" aria-label="Person walking two small dogs on leashes" style="background:linear-gradient(160deg,#b7c79a,#6f7f6a)"><div class="date">27<small>June</small></div></div>
    <h3>Lorem Ipsum typesetting industry.</h3>
    <p>Lorem Ipsum is simply dummy text of printing and typesetting industry. Lorem  dummy text ever since the 1500s</p>
    <a>READ MORE</a>
  </article>
  <article class="post" style="left:434px">
    <div class="img" role="img" aria-label="Two small dogs running outdoors" style="background:linear-gradient(160deg,#d9b48c,#8e6a4c)"><div class="date">27<small>June</small></div></div>
    <h3>Lorem Ipsum typesetting industry.</h3>
    <p>Lorem Ipsum is simply dummy text of printing and typesetting industry. Lorem  dummy text ever since the 1500s</p>
    <a>READ MORE</a>
  </article>
  <article class="post" style="left:790px">
    <div class="img" role="img" aria-label="Hand petting a relaxed cat" style="background:linear-gradient(160deg,#c9843a,#7a4c26)"><div class="date">27<small>June</small></div></div>
    <h3>Lorem Ipsum typesetting industry.</h3>
    <p>Lorem Ipsum is simply dummy text of printing and typesetting industry. Lorem  dummy text ever since the 1500s</p>
    <a>READ MORE</a>
  </article>
</section>

<section class="newsletter" role="img" aria-label="Green tinted photo of a pet owner with a dog">
  <h2>SUBSCRIBE TO OUR NEWSLETTER &amp; GET 10% OFF</h2>
  <div class="sub">SIGN UP AND GET YOUR WELCOME PRESENT TODAY</div>
  <div class="email-field">Email Address
    <svg width="34" height="26" viewBox="0 0 34 26"><path d="M2 12L32 2 22 24l-6-8z" fill="none" stroke="#1f5a3a" stroke-width="2.5" stroke-linejoin="round"/><path d="M16 16L32 2" stroke="#1f5a3a" stroke-width="2.5"/></svg>
  </div>
</section>

<footer class="site-footer">
  <div class="foot-brand"><i></i>KINDRED PAW</div>
  <p class="foot-about">Lorem Ipsum is simply dummy text printing...(+)</p>
  <div class="col where" style="left:292px">
    <h4>WHERE</h4>
    <div><svg width="18" height="18" viewBox="0 0 24 24"><path fill="#1a8ad4" d="M6.6 10.8a15.1 15.1 0 006.6 6.6l2.2-2.2c.3-.3.7-.4 1-.2 1.1.4 2.3.6 3.6.6.6 0 1 .4 1 1V20c0 .6-.4 1-1 1A17 17 0 013 4c0-.6.4-1 1-1h3.5c.6 0 1 .4 1 1 0 1.3.2 2.5.6 3.6.1.3 0 .7-.2 1z"/></svg>(123) 456 789</div>
    <div><svg width="18" height="14" viewBox="0 0 24 18"><rect x="1" y="1" width="22" height="16" rx="2" fill="#1a8ad4"/><path d="M1 2l11 8 11-8" stroke="#fff" stroke-width="2" fill="none"/></svg>care@kindredpaw.example</div>
    <div><svg width="16" height="20" viewBox="0 0 16 22"><path d="M8 0a8 8 0 00-8 8c0 6 8 14 8 14s8-8 8-14a8 8 0 00-8-8z" fill="#1a8ad4"/><circle cx="8" cy="8" r="3" fill="#fff"/></svg>123, Address, State<br>Name, City ,Zipcode</div>
  </div>
  <div class="col" style="left:506px">
    <h4>QUICK LINKS</h4>
    <ul><li>Home</li><li>Our Story</li><li>Products</li><li>Benefits</li><li>Blog</li><li>Contact</li></ul>
  </div>
  <div class="col" style="left:718px">
    <h4>HELP</h4>
    <ul><li>FAQs</li><li>Privacy</li><li>terms &amp; Conditions</li></ul>
  </div>
  <div class="col" style="left:931px">
    <h4>GET SOCIAL</h4>
    <div class="socials"><span style="background:#3b5998"></span><span style="background:#0e76a8"></span><span style="background:#c1358a"></span><span style="background:#1da1f2"></span></div>
  </div>
  <div class="copyright">Copyright © KINDRED PAW WELLNESS - 2019 . All Right Reserved</div>
</footer>

</body>
</html>
```